Moltbeck Chardonnay Wine Label 2024

We need a wine label design for a small, family-owned vineyard in Broke, Hunter Valley of NSW (Australia). The vineyard is called Moltbeck and we have an existing logo and 'brand book' for the vineyard home that is rented out for short stay bookings. This is attached and includes font style, colour palette and our Moltbeck logo for the accommodation (we're not wedded to this but also probably not after a completely different rethink either as we want the accommodation and the wine to feel part of the same thing.

Project:
The initial label requirement (front and back) is for the Moltbeck 2024 Chardonnay, which is called 'Juniper'. The label would need to be able to extend to other varietals (eg Verdehlo and Sparkling) in 2025. Attached is draft copy for front and back for the 2024 Chardonnay as a guide.

STYLE: We like a relatively simple, classic design and have played with both a dark (navy) and a light background (white/cream). Based on the final label design we will order a Kortap colour to pick up on the label theme.

The Chardonnay bottle dimensions are attached, as is our logo file (if that helps)

online 25-50 yearold

Wine

• front and back label design Moltbeck logo and name

```html
<!DOCTYPE html>
<html lang="en">
<head>
<meta charset="utf-8">
<title>Moltbeck Juniper 2024 Chardonnay – Front Label</title>
<link rel="stylesheet" href="https://fonts.googleapis.com/css2?family=Libre+Baskerville:wght@400&family=Montserrat:wght@600;700&display=swap">
<style>
  :root {
    --navy: #2f3a52;
    --paper: #f7f7f6;
    --contour: #e6e7ea;
    --taupe: #8a7c66;
    --backdrop: #ecebe8;
    --white: #ffffff;
  }
  html, body {
    margin: 0;
    width: 1200px;
    height: 1120px;
    overflow: hidden;
    background: var(--backdrop);
  }
  .label {
    position: absolute;
    left: 220px;
    top: 60px;
    width: 760px;
    height: 1000px;
    background: var(--paper);
    box-shadow: 0 2px 14px rgba(0,0,0,0.08);
    overflow: hidden;
    text-align: center;
    color: var(--navy);
  }
  .label__terrain {
    position: absolute;
    inset: 0;
    background:
      radial-gradient(ellipse at 30% 30%, var(--paper) 0%, var(--contour) 60%, var(--paper) 100%),
      var(--paper);
    opacity: 0.7;
  }
  .label__content {
    position: relative;
    height: 100%;
  }
  .brand {
    position: absolute;
    top: 150px;
    left: 0;
    right: 0;
    font-family: "Libre Baskerville", Georgia, serif;
    font-size: 84px;
    letter-spacing: -1px;
    line-height: 1;
  }
  .brand__dot {
    position: absolute;
    top: -70px;
    left: 520px;
    width: 70px;
    height: 70px;
    border-radius: 50%;
    background: var(--navy);
  }
  .wine-name {
    position: absolute;
    top: 400px;
    left: 60px;
    right: 60px;
    height: 90px;
    background: var(--navy);
    color: var(--white);
    font-family: "Montserrat", Arial, sans-serif;
    font-weight: 700;
    font-size: 62px;
    letter-spacing: 22px;
    line-height: 90px;
    text-indent: 22px;
  }
  .vintage {
    position: absolute;
    top: 555px;
    left: 0;
    right: 0;
    font-family: "Libre Baskerville", Georgia, serif;
    font-size: 64px;
    color: var(--taupe);
    line-height: 1;
  }
  .varietal {
    position: absolute;
    top: 660px;
    left: 0;
    right: 0;
    font-family: "Libre Baskerville", Georgia, serif;
    font-size: 54px;
    letter-spacing: 14px;
    text-indent: 14px;
    line-height: 1;
  }
  .region {
    position: absolute;
    top: 760px;
    left: 115px;
    right: 115px;
    height: 76px;
    background: var(--navy);
    color: var(--white);
    font-family: "Montserrat", Arial, sans-serif;
    font-weight: 600;
    font-size: 40px;
    letter-spacing: 3px;
    line-height: 76px;
  }
  .volume {
    position: absolute;
    top: 875px;
    left: 0;
    right: 0;
    font-family: "Libre Baskerville", Georgia, serif;
    font-size: 48px;
    line-height: 1;
  }
</style>
</head>
<body>
  <main class="label">
    <div class="label__terrain" role="img" aria-label="Fine grey topographic contour-line pattern across the label"></div>
    <div class="label__content">
      <div class="brand">Moltbeck<span class="brand__dot"></span></div>
      <div class="wine-name">JUNIPER</div>
      <div class="vintage">2024</div>
      <div class="varietal">CHARDONNAY</div>
      <div class="region">HUNTER VALLEY</div>
      <div class="volume">750ml</div>
    </div>
  </main>
</body>
</html>
```